Broadcaster,Conference Host,Facilitator

Looking for a business card and logo to create the Grant Ollerby brand .. Something with a slant towards radio and conference speaking
I like the idea of classic black white or grey but open to suggestions

Target Market(s)

Corporates

Industry/Entity Type

Business

Contact Information for Business Card

Grant Ollerby
Email : Grant.Ollerby@fenmail.co.uk
Mobile : +44 7700 384216
Twitter : @Grantollerby

Font styles to use
Serif
Decorative
Script

Requirements
Must have
• Feel classy and dynamic
Should not have
• Cartoons

```html
<!DOCTYPE html>
<html lang="en">
<head>
<meta charset="utf-8">
<title>Grant Ollerby – Business Card</title>
<link href="https://fonts.googleapis.com/css2?family=Great+Vibes&family=Open+Sans:wght@400;700&display=swap" rel="stylesheet">
<style>
  :root {
    --canvas: #e4e2de;
    --ink-black: #1f1d1d;
    --card-black: #252323;
    --paper: #f4f4f3;
    --paper-shade: #e2e2e1;
    --silver: #a9a9aa;
    --silver-light: #c9c9ca;
    --text-dark: #1c1c1c;
    --text-light: #f2f2f2;
  }
  html, body {
    margin: 0;
    padding: 0;
    width: 1200px;
    height: 780px;
    overflow: hidden;
    background: var(--canvas);
  }
  .stage {
    position: relative;
    width: 1200px;
    height: 780px;
    display: flex;
    align-items: center;
    justify-content: center;
    gap: 60px;
  }
  .card {
    width: 525px;
    height: 300px;
    box-shadow: 0 10px 28px rgba(0,0,0,0.25);
  }
  .card svg { display: block; }
  .script-name {
    font-family: "Great Vibes", cursive;
  }
  .contact-line {
    font-family: "Open Sans", sans-serif;
    font-size: 13px;
  }
  .contact-label { font-weight: 700; }
  .mark-name {
    font-family: "Open Sans", sans-serif;
    font-size: 11px;
    font-weight: 400;
    letter-spacing: 0.5px;
  }
</style>
</head>
<body>
<main class="stage">

  <section class="card card-front" aria-label="Business card front">
    <svg width="525" height="300" viewBox="0 0 525 300">
      <defs>
        <linearGradient id="paperGradient" x1="0" y1="0" x2="1" y2="1">
          <stop offset="0" stop-color="var(--paper-shade)"/>
          <stop offset="0.5" stop-color="var(--paper)"/>
          <stop offset="1" stop-color="var(--paper-shade)"/>
        </linearGradient>
      </defs>
      <rect class="card-base" width="525" height="300" fill="var(--card-black)"/>
      <path class="panel-rim" d="M0,88 Q250,70 525,6 L525,236 Q300,272 0,292 Z" fill="var(--silver)"/>
      <path class="info-panel" d="M0,96 Q250,78 525,14 L525,228 Q300,264 0,284 Z" fill="url(#paperGradient)"/>
      <path class="panel-line" d="M0,102 Q250,84 525,20" fill="none" stroke="var(--silver-light)" stroke-width="1"/>
      <path class="panel-line" d="M0,278 Q300,258 525,222" fill="none" stroke="var(--silver-light)" stroke-width="1"/>

      <g class="brand-mark">
        <circle cx="118" cy="92" r="50" fill="var(--ink-black)" stroke="var(--silver-light)" stroke-width="3"/>
        <text class="mark-name" x="118" y="96" text-anchor="middle" fill="var(--text-light)">Grant Ollerby</text>
      </g>

      <text class="script-name" x="150" y="166" font-size="46" fill="var(--text-dark)">Grant Ollerby</text>

      <g class="contact-details" fill="var(--text-dark)">
        <text class="contact-line" x="200" y="194"><tspan class="contact-label">Email :</tspan> Grant.Ollerby@fenmail.co.uk</text>
        <text class="contact-line" x="200" y="213"><tspan class="contact-label">Mobile :</tspan> +44 7700 384216</text>
        <text class="contact-line" x="200" y="232"><tspan class="contact-label">Twitter :</tspan> @Grantollerby</text>
      </g>
    </svg>
  </section>

  <section class="card card-back" aria-label="Business card back">
    <svg width="525" height="300" viewBox="0 0 525 300">
      <defs>
        <linearGradient id="sweepGradient" x1="0" y1="0" x2="1" y2="0">
          <stop offset="0" stop-color="#8e8e8f"/>
          <stop offset="1" stop-color="var(--silver-light)"/>
        </linearGradient>
      </defs>
      <rect class="card-base" width="525" height="300" fill="var(--card-black)"/>
      <path class="silver-sweep" d="M0,232 Q260,300 525,300 L0,300 Z" fill="url(#sweepGradient)"/>
      <path class="sweep-edge" d="M0,232 Q260,300 525,300" fill="none" stroke="#3a3838" stroke-width="2"/>

      <g class="brand-mark">
        <circle cx="330" cy="112" r="52" fill="var(--paper)" stroke="var(--silver)" stroke-width="3"/>
        <text class="mark-name" x="330" y="116" text-anchor="middle" fill="var(--text-dark)">Grant Ollerby</text>
      </g>

      <text class="script-name" x="232" y="210" text-anchor="middle" font-size="48" fill="var(--text-light)">Grant Ollerby</text>
    </svg>
  </section>

</main>
</body>
</html>
```